Text heavy poster for university audience

I have developed a set of standards for online teaching that need to be turned into a post format. The project has a logo which should be incorporated. Most of the designing will be in terms of text layout. The logo (two versions - higher quality files available) and the a sample of standards (as image - word version available; the example is one third of standards) are attached. Design that can be adapted to brochure format would be great. (Brochure adaption will be paid separately via another project to be opened here). More details available here: http://www.brivelquarto.net
Updates

Dear all,

The URL for the site needs to be include in the design - either as footer or under logo:
<http://www.brivelquarto.net>

Sorry for late notice

Target Market(s)

The are university staff

Industry/Entity Type

University

Font styles to use
Serif
Sans Serif

Requirements
Must have
• The text in the "required" attachment must be included; but for initial draft feel free to restrict your design to "sample" attachment
The green from the Logo (PANTONE 17-5641 Emerald) should be the foundation of the colour palette.
Nice to have
• The collaborators as named here: http://www.brivelquarto.net/collaborators/
My preferred find is helvetica neue, but similar can be used
Should not have
• Decorative fonts

```html
<!DOCTYPE html>
<html lang="en">
<head>
<meta charset="utf-8">
<title>Brivel Quarto – Standards for Online Teaching</title>
<link rel="stylesheet" href="https://fonts.googleapis.com/css2?family=Arimo:wght@400;700&display=swap">
<style>
  :root {
    --emerald: #009473;
    --emerald-dark: #007a5e;
    --label-green: #2f9f78;
    --ink: #1f2a26;
    --rule: #cfd8d4;
    --paper: #ffffff;
    --frame: #e4ebe8;
  }
  * { box-sizing: border-box; margin: 0; padding: 0; }
  html, body { width: 865px; height: 1200px; overflow: hidden; background: var(--paper); }
  body { font-family: "Arimo", "Helvetica Neue", Arial, sans-serif; color: var(--ink); }

  .poster { width: 865px; height: 1200px; display: flex; flex-direction: column; border: 6px solid var(--frame); }

  .masthead {
    height: 92px; background: var(--emerald); display: flex; align-items: center;
    justify-content: space-between; padding: 0 28px;
  }
  .brand { display: flex; align-items: center; gap: 12px; color: #fff; font-weight: 700; font-size: 30px; letter-spacing: 0.5px; }
  .brand-mark { width: 26px; height: 26px; background: #fff; }
  .authors { color: #fff; font-weight: 700; font-size: 26px; }

  .intro {
    padding: 16px 28px 10px; color: var(--emerald-dark); font-weight: 700; font-size: 17px; line-height: 1.35;
  }

  .standards { flex: 1; padding: 0 28px; display: flex; flex-direction: column; justify-content: space-between; }
  .standard h2 { font-size: 16px; color: var(--emerald-dark); font-weight: 700; margin-bottom: 5px; }
  .levels { width: 100%; border-collapse: collapse; font-size: 12.5px; }
  .levels tr { border-top: 1px solid var(--rule); }
  .levels tr:last-child { border-bottom: 1px solid var(--rule); }
  .levels th {
    width: 128px; height: 26px; background: var(--label-green); color: #fff; font-weight: 400;
    text-align: left; padding: 0 10px; border-bottom: 2px solid #fff;
  }
  .levels td { padding: 0 12px; }

  .footer { display: flex; align-items: center; gap: 14px; padding: 12px 28px 14px; }
  .licence-badge { width: 78px; height: 28px; flex: none; background: #d5ddd9; border-radius: 3px; }
  .footer p { font-size: 8.5px; line-height: 1.35; color: #55625d; }
</style>
</head>
<body>
<main class="poster">
  <header class="masthead">
    <div class="brand"><span class="brand-mark"></span>Brivel Quarto</div>
    <div class="authors">Dara Wenlock and Collaborators</div>
  </header>

  <p class="intro">Students are supported in their online learning with a quality curriculum [1-4], opportunities for interaction with peers and staff [5&amp;6], and appropriate support [7&amp;8].</p>

  <section class="standards">
    <article class="standard">
      <h2>1. Curriculum materials are aligned, available and engaging</h2>
      <table class="levels">
        <tr><th>Threshold</th><td>The necessary materials are constructively aligned and available online</td></tr>
        <tr><th>Good</th><td>The materials are provided using a variety of media to engage students and support diversity</td></tr>
        <tr><th>Excellent</th><td></td></tr>
      </table>
    </article>
    <article class="standard">
      <h2>2. Learning activities are aligned, available and engaging</h2>
      <table class="levels">
        <tr><th>Threshold</th><td>Constructively aligned learning activities are available online</td></tr>
        <tr><th>Good</th><td>Learning activities use a variety of appropriate technologies to engage students and support diversity</td></tr>
        <tr><th>Excellent</th><td></td></tr>
      </table>
    </article>
    <article class="standard">
      <h2>3. Assessment tasks are aligned, available and engaging</h2>
      <table class="levels">
        <tr><th>Threshold</th><td>Constructively aligned assessment tasks are available online</td></tr>
        <tr><th>Good</th><td>Assessment tasks use a variety of appropriate technologies to engage students and support diversity</td></tr>
        <tr><th>Excellent</th><td></td></tr>
      </table>
    </article>
    <article class="standard">
      <h2>4. Students are provided with timely, improvement focused formative feedback</h2>
      <table class="levels">
        <tr><th>Threshold</th><td>Appropriate technologies are used to provide students with formative feedback in a timely manner</td></tr>
        <tr><th>Good</th><td>Feedback is provided in a variety of media to engage students and support diversity</td></tr>
        <tr><th>Excellent</th><td></td></tr>
      </table>
    </article>
    <article class="standard">
      <h2>5. Students are provided with opportunities to interact with peers</h2>
      <table class="levels">
        <tr><th>Threshold</th><td>There are opportunities for social interaction</td></tr>
        <tr><th>Good</th><td>There are opportunities for learning-focused interaction</td></tr>
        <tr><th>Excellent</th><td></td></tr>
      </table>
    </article>
    <article class="standard">
      <h2>6. Students are provided with opportunities to interact with staff</h2>
      <table class="levels">
        <tr><th>Threshold</th><td>Staff are provided with opportunities to answer student queries</td></tr>
        <tr><th>Good</th><td>Staff are provided with opportunities to be active participants in learning-focused interactions</td></tr>
        <tr><th>Excellent</th><td></td></tr>
      </table>
    </article>
    <article class="standard">
      <h2>7. Students are provided with appropriate learning support</h2>
      <table class="levels">
        <tr><th>Threshold</th><td>Appropriate, up-to-date and reliable learning guides and resources are provided online</td></tr>
        <tr><th>Good</th><td>A range of appropriate, up-to-date and reliable online learning skills workshops are available</td></tr>
        <tr><th>Excellent</th><td></td></tr>
      </table>
    </article>
    <article class="standard">
      <h2>8. Students are supported in their use of educational technology</h2>
      <table class="levels">
        <tr><th>Threshold</th><td>Appropriate, up-to-date and reliable technological guides and resources are provided online</td></tr>
        <tr><th>Good</th><td>Appropriate, timely and reliable asynchronous technological support is available</td></tr>
        <tr><th>Excellent</th><td></td></tr>
      </table>
    </article>
  </section>

  <footer class="footer">
    <div class="licence-badge" role="img" aria-label="Open licence badge"></div>
    <p>This poster is shared under an open licence that allows copying and adaptation with attribution. Support for this work was provided by a national teaching grant. The views expressed do not necessarily reflect those of the funding body. Full terms and the complete list of standards are available online from the project team: http://www.brivelquarto.net</p>
  </footer>
</main>
</body>
</html>
```